Bright Stride Clinic helping older adults use exercise as medicine

We need a website for a start up company providing exercise physiology and physiotherapy clinical services for people with serious health conditions such as cancer, diabetes and many others This is an exculsive service with limited time. The 2 main objectives of the website are to create leads for appointments and provide education about the benefits of exercise ie stretches, strength training, cardio vascular improvement for people with health conditions.
Please not too medical in design more fitness and lifestyle... sell the promise, please sell happy fit active people.

Target Market(s)

40-70 year old adults both male and female interested in a healthy lifestyle, ie baby boomers moderate education level (finished high school minimum) rural/country people

Industry/Entity Type

Health

Number of Pages Required

4 page

Font styles to use
Serif
Sans Serif

Colors
f26f22
3176b5

Requirements
Must have
• Website must have a blog/education area and a members area with access to an exercise database (picture, description and video)

```html
<!DOCTYPE html>
<html lang="en">
<head>
<meta charset="utf-8">
<title>Bright Stride Clinic</title>
<link rel="stylesheet" href="https://fonts.googleapis.com/css2?family=Lato:wght@400;700&family=Open+Sans:wght@400;600&family=Norican&display=swap">
<style>
:root{
  --orange:#d9560a;
  --orange-light:#e0702c;
  --navy:#0b347f;
  --navy-deep:#0a3a84;
  --text:#333;
  --muted:#555;
  --grey-band:#f2f2f2;
  --line:#ddd;
  --white:#fff;
}
*{box-sizing:border-box;margin:0;padding:0}
html,body{width:1000px;height:1200px;overflow:hidden;background:var(--white)}
body{position:relative;font-family:"Open Sans",Arial,sans-serif;color:var(--text)}
.abs{position:absolute}

/* header */
.site-header{position:absolute;left:0;top:0;width:1000px;height:110px;border-bottom:3px solid #d6d6d6}
.corner-swoosh{position:absolute;left:0;top:0}
.call{position:absolute;left:226px;top:20px;display:flex;gap:8px;align-items:center}
.call-label{font-family:"Lato",sans-serif;font-size:11.5px;letter-spacing:1.6px;font-weight:700;color:#222}
.call-number{font-family:"Lato",sans-serif;font-size:16px;font-weight:700;color:#222;letter-spacing:.4px}
.main-nav{position:absolute;left:126px;top:80px;display:flex;font-family:"Lato",sans-serif;font-size:13px;font-weight:700;color:#222}
.main-nav span{padding:0 7px;border-left:1px solid #ccc;line-height:14px}
.main-nav span:first-child{padding-left:0;border:0;color:var(--orange)}
.brand{position:absolute;right:116px;top:52px;display:flex;align-items:center;gap:7px;font-family:"Lato",sans-serif;font-weight:700;font-size:19px;color:var(--navy)}
.brand-dot{width:14px;height:14px;border-radius:50%;background:var(--orange)}

/* hero */
.hero{position:absolute;left:0;top:110px;width:1000px;height:405px;
  background:linear-gradient(180deg,#7aa6d4 0%,#a9c7e3 42%,#d9cbb0 56%,#e6d6bb 75%,#d3bc98 100%)}
.hero-tagline{position:absolute;left:470px;top:92px;width:395px;text-align:center;font-family:"Norican",cursive;font-size:31px;line-height:40px;color:#1e1e1e;text-shadow:0 0 6px rgba(255,255,255,.6)}
.hero-dots{position:absolute;left:816px;top:385px;display:flex;gap:9px}
.hero-dots i{width:15px;height:4px;background:#333}
.hero-dots i:first-child{background:var(--orange)}
.hero-shadow{position:absolute;left:20px;top:515px;width:960px;height:18px;background:radial-gradient(ellipse at top,rgba(0,0,0,.35),rgba(0,0,0,0) 70%)}

/* feature tiles */
.features{position:absolute;left:117px;top:553px;width:766px;height:102px;display:flex}
.feature{flex:1;background:var(--orange);color:var(--white);display:flex;flex-direction:column;align-items:center;justify-content:flex-end;padding-bottom:8px;font-family:"Lato",sans-serif;font-weight:700;font-size:19.5px;gap:12px}
.feature.alt{background:var(--orange-light)}

/* panels */
.panel{position:absolute;top:690px;width:242px;height:218px;background:var(--white);border:1px solid #e3e3e3;box-shadow:0 6px 6px -4px rgba(0,0,0,.3);overflow:hidden}
.panel-head{height:34px;background:var(--navy);color:var(--white);font-family:"Lato",sans-serif;font-weight:700;font-size:18px;line-height:34px;padding-left:47px;position:relative}
.panel-badge{position:absolute;left:3px;top:1px;width:34px;height:34px;border-radius:50%;background:var(--white);border:2px solid #ddd}
.panel-badge::after{content:"";position:absolute;left:11px;top:11px;width:8px;height:8px;border-radius:50%;background:var(--orange)}
.panel-corner{position:absolute;right:0;bottom:0}
.about-body{padding:6px 12px 0 13px;font-size:11.2px;line-height:16.5px;color:#333}
.about-body strong{display:block;font-weight:600;color:#111;margin-bottom:2px}
.why-list{list-style:none;padding:4px 14px 0 14px}
.why-list li{font-size:11px;font-weight:600;color:#111;height:33.5px;line-height:33px;border-bottom:1px solid #e6e6e6;display:flex;align-items:center;gap:5px}
.why-list li:last-child{border:0}
.why-list li::before{content:"";width:5px;height:14px;background:var(--orange);border-radius:2px}
.field{margin:0 16px 8px 16px;height:24px;border:1px solid #cfcfcf;border-radius:2px;font-size:11px;color:#555;display:flex;align-items:center;gap:8px;padding-left:7px}
.field.message{height:51px;align-items:flex-start;padding-top:5px}
.contact-form{padding-top:11px}

/* blog */
.blog-band{position:absolute;left:0;top:941px;width:1000px;height:160px;background:linear-gradient(180deg,#efefef,#fafafa)}
.blog-title{position:absolute;left:119px;top:958px;font-family:"Lato",sans-serif;font-weight:700;font-size:19px;color:var(--navy)}
.blog-rule{position:absolute;left:117px;top:986px;width:766px;height:1px;background:#cfcfcf}
.blog-arrows{position:absolute;left:845px;top:964px;display:flex;gap:6px}
.post{position:absolute;top:1004px;width:366px}
.post-photo{position:absolute;left:0;top:0;width:64px;height:64px;border-radius:50%;border:3px solid #fff;box-shadow:0 0 0 1px #ccc}
.post-title{position:absolute;left:77px;top:3px;font-size:11.5px;font-weight:600;color:#111}
.post-date{position:absolute;right:0;top:4px;font-size:11.5px;font-weight:600;color:#111}
.post-text{position:absolute;left:77px;top:22px;width:290px;font-size:11px;line-height:20px;color:#333}
.post-more{position:absolute;right:0;top:62px;font-size:12px;font-weight:600;color:var(--navy)}
.post-divider{position:absolute;left:500px;top:1000px;width:2px;height:80px;background:linear-gradient(180deg,rgba(0,0,0,0),rgba(0,0,0,.12),rgba(0,0,0,0))}

/* footer */
.site-footer{position:absolute;left:0;top:1101px;width:1000px;height:99px;background:var(--navy-deep);color:var(--white);font-size:11.5px}
.footer-nav{position:absolute;left:119px;top:11px;display:flex;font-family:"Lato",sans-serif;font-size:11.5px}
.footer-nav span{padding:0 7px;border-left:1px solid rgba(255,255,255,.35)}
.footer-nav span:first-child{padding-left:0;border:0}
.footer-line{position:absolute;left:119px;display:flex;align-items:center;gap:10px}
.social{position:absolute;left:769px;top:19px;display:flex;gap:8px}
.social i{width:18px;height:18px;background:var(--white);border-radius:2px}
.copyright{position:absolute;left:740px;top:52px;width:150px;text-align:center;line-height:15px;font-size:11.5px}
</style>
</head>
<body>

<header class="site-header">
  <svg class="corner-swoosh" width="280" height="104" viewBox="0 0 280 104">
    <path d="M0 0H280C200 10 120 40 0 92Z" fill="var(--orange)"/>
    <path d="M0 92C120 40 200 10 280 0" fill="none" stroke="var(--navy)" stroke-width="5"/>
    <path d="M0 100C120 48 200 16 280 4" fill="none" stroke="var(--white)" stroke-width="3"/>
  </svg>
  <div class="call">
    <svg width="30" height="30" viewBox="0 0 30 30"><circle cx="15" cy="15" r="13.5" fill="none" stroke="var(--navy)" stroke-width="2"/><path d="M10 8l3 0 1 4-2 1.5c1 2 2.5 3.5 4.5 4.5L18 16l4 1v3c-7 1-13-5-12-12z" fill="var(--navy)"/></svg>
    <div><div class="call-label">CALL US TODAY</div><div class="call-number">012-555-0147</div></div>
  </div>
  <nav class="main-nav"><span>Home</span><span>About Us</span><span>Accredited Exercise Physiologist</span><span>Services</span><span>Contact Us</span></nav>
  <div class="brand"><span class="brand-dot"></span>Bright Stride Clinic</div>
</header>

<section class="hero" role="img" aria-label="Photo of a smiling older couple running hand in hand down a sunny beach dune">
  <p class="hero-tagline">Lorem ipsum dolor sit amet, consectetuer adipiscing elit, sed diam nonummy</p>
  <div class="hero-dots"><i></i><i></i><i></i></div>
</section>
<div class="hero-shadow"></div>

<section class="features">
  <div class="feature">
    <svg width="46" height="46" viewBox="0 0 46 46"><circle cx="28" cy="7" r="5" fill="#fff"/><circle cx="11" cy="34" r="9" fill="#fff"/><path d="M18 16l12-2 4 12 8 10" fill="none" stroke="#fff" stroke-width="5" stroke-linecap="round" stroke-linejoin="round"/></svg>
    STRETCHES
  </div>
  <div class="feature alt">
    <svg width="48" height="46" viewBox="0 0 48 46"><rect x="6" y="20" width="36" height="5" fill="#fff"/><rect x="2" y="13" width="6" height="19" rx="1" fill="#fff"/><rect x="40" y="13" width="6" height="19" rx="1" fill="#fff"/><rect x="17" y="28" width="14" height="18" fill="#fff"/></svg>
    STRENGTH TRAINING
  </div>
  <div class="feature">
    <svg width="48" height="44" viewBox="0 0 48 44"><path d="M24 42C8 30 2 22 2 13 2 6 8 1 14 1c4 0 8 2 10 6 2-4 6-6 10-6 6 0 12 5 12 12 0 9-6 17-22 29z" fill="#fff"/><path d="M6 22h12l3-6 4 12 3-6h14" fill="none" stroke="var(--orange)" stroke-width="2.5"/></svg>
    CARDIO IMPROVEMENT
  </div>
</section>

<article class="panel" style="left:117px">
  <h2 class="panel-head"><span class="panel-badge"></span>About Us</h2>
  <div class="about-body">
    <strong>Ut wisi nim ad minim veniam, quis exetiper suscipit lobortis nisl ut aliquip ex ea comm</strong>
    Lorem ipsum dolor sit amet, constu The adipiscing elit, sed diam nonummy nibh euismod laoreet dolore magna aliquam erat volutpat. Ut winim ad minim veniam, quis nostrud exetip isuiscipit lobortis nisl ut aliquip ex ea comm consequait
  </div>
  <svg class="panel-corner" width="40" height="40" viewBox="0 0 40 40"><path d="M40 0V40H0Z" fill="var(--orange)"/><path d="M27 24v12M21 30h12" stroke="#fff" stroke-width="2.5"/></svg>
</article>

<article class="panel" style="left:379px">
  <h2 class="panel-head"><span class="panel-badge"></span>Why Choose Us</h2>
  <ul class="why-list">
    <li>Lorem ipsum dolor sit amet constu</li>
    <li>Lorem ipsum dolor sit amet constu</li>
    <li>Lorem ipsum dolor sit amet constu</li>
    <li>Lorem ipsum dolor sit amet constu</li>
    <li>Lorem ipsum dolor sit amet constu</li>
  </ul>
  <svg class="panel-corner" width="40" height="40" viewBox="0 0 40 40"><path d="M40 0V40H0Z" fill="var(--orange)"/><path d="M27 24v12M21 30h12" stroke="#fff" stroke-width="2.5"/></svg>
</article>

<article class="panel" style="left:641px">
  <h2 class="panel-head"><span class="panel-badge"></span>Quick Contact</h2>
  <div class="contact-form">
    <div class="field"><svg width="12" height="12" viewBox="0 0 12 12"><circle cx="6" cy="3.5" r="3" fill="#555"/><path d="M0 12c0-4 3-5 6-5s6 1 6 5z" fill="#555"/></svg>Name</div>
    <div class="field"><svg width="12" height="10" viewBox="0 0 12 10"><rect width="12" height="10" fill="#555"/><path d="M0 0l6 5 6-5" fill="none" stroke="#fff"/></svg>Email</div>
    <div class="field"><svg width="12" height="12" viewBox="0 0 12 12"><path d="M2 1h3l1 3-2 1c1 1.5 2 2.5 3 3l1-2 3 1v3C6 11 1 6 2 1z" fill="#555"/></svg>Phone</div>
    <div class="field message"><svg width="12" height="12" viewBox="0 0 12 12"><rect x=".5" y="2" width="9" height="9.5" fill="none" stroke="#555"/><path d="M5 7l6-6" stroke="#555" stroke-width="1.6"/></svg>Message</div>
  </div>
  <svg class="panel-corner" width="40" height="40" viewBox="0 0 40 40"><path d="M40 0V40H0Z" fill="var(--orange)"/><path d="M27 24v12M21 30h12" stroke="#fff" stroke-width="2.5"/></svg>
</article>

<section class="blog-band"></section>
<h2 class="blog-title">Recent Blog Posts</h2>
<div class="blog-rule"></div>
<div class="blog-arrows">
  <svg width="16" height="16" viewBox="0 0 16 16"><circle cx="8" cy="8" r="7" fill="none" stroke="#333" stroke-width="1.2"/><path d="M9.5 4.5L6 8l3.5 3.5" fill="none" stroke="#333" stroke-width="1.4"/></svg>
  <svg width="16" height="16" viewBox="0 0 16 16"><circle cx="8" cy="8" r="7" fill="none" stroke="var(--navy)" stroke-width="1.2"/><path d="M6.5 4.5L10 8l-3.5 3.5" fill="none" stroke="var(--navy)" stroke-width="1.4"/></svg>
</div>

<article class="post" style="left:118px">
  <div class="post-photo" role="img" aria-label="Photo of a smiling woman in fitness wear" style="background:linear-gradient(160deg,#c9a27e,#6b8fb8)"></div>
  <h3 class="post-title">Lorem ipsum dolor sit amet</h3>
  <span class="post-date">08-OCT 2014</span>
  <p class="post-text">sed dia nonumi consect uerol adipiscing sed dia nonum nibh consel The uerol adipiscing elit uerol adipiscing sed</p>
  <span class="post-more">Lorem ipsum</span>
</article>
<div class="post-divider"></div>
<article class="post" style="left:520px">
  <div class="post-photo" role="img" aria-label="Photo of a smiling woman eating fresh fruit" style="background:linear-gradient(160deg,#e8d2b4,#d9a05f)"></div>
  <h3 class="post-title">Lorem ipsum dolor sit amet</h3>
  <span class="post-date">09-OCT 2014</span>
  <p class="post-text">sed dia nonumi consect uerol adipiscing sed dia nonum nibh consel The uerol adipiscing elit uerol adipiscing sed</p>
  <span class="post-more">Lorem ipsum</span>
</article>

<footer class="site-footer">
  <nav class="footer-nav"><span>Home</span><span>About Us</span><span>Accredited Exercise Physiologist</span><span>Services</span><span>Contact Us</span></nav>
  <div class="footer-line" style="top:41px">
    <svg width="12" height="16" viewBox="0 0 12 16"><path d="M6 16C2 10 0 8 0 6a6 6 0 0112 0c0 2-2 4-6 10z" fill="#d8dde8"/><circle cx="6" cy="6" r="2.2" fill="var(--navy-deep)"/></svg>
    <span style="margin-left:4px">Lorem ipsum dolor sit amet, consecti ulm adipiscin elit</span>
  </div>
  <div class="footer-line" style="top:66px">
    <svg width="14" height="14" viewBox="0 0 12 12"><path d="M2 1h3l1 3-2 1c1 1.5 2 2.5 3 3l1-2 3 1v3C6 11 1 6 2 1z" fill="#d8dde8"/></svg>
    <span style="margin-left:6px">012-555-0147</span>
    <svg width="16" height="11" viewBox="0 0 16 11" style="margin-left:10px"><rect width="16" height="11" fill="#d8dde8"/><path d="M0 0l8 6 8-6" fill="none" stroke="var(--navy-deep)"/></svg>
    <span>hello@brightstride.com</span>
  </div>
  <div class="social"><i></i><i></i><i></i><i></i></div>
  <p class="copyright">© 2014 Bright Stride Clinic<br>All Rights Reserved</p>
</footer>

</body>
</html>
```